Business Card Design for Miss Poppy's Soak Parlour

Name: Miss Poppy's Soak Parlour. Maker of bath bombs, bath salts.

Card details:

Donna Pickett
1.702.555.0143
Las Vegas Nevada
dpickett47@mailpost.example

"Bath bombs, bath salts and more..."

A picture of an old-fashioned bathtub (with claw feet) filled with bath bombs.

Colors include: Lavender, Pink, Turquois, Light Blue. Can you make the overall design look old fashioned.

```html
<!DOCTYPE html>
<html lang="en">
<head>
<meta charset="utf-8">
<title>Miss Poppy's Soak Parlour – Business Cards</title>
<link href="https://fonts.googleapis.com/css2?family=Arimo&family=Marcellus&display=swap" rel="stylesheet">
<style>
  :root {
    --stage: #0e0e0e;
    --lavender: #cdbde0;
    --lavender-deep: #b7a6d6;
    --pink: #eab4cf;
    --peach: #f1c9bd;
    --turquoise: #7fc3cf;
    --light-blue: #a9c9e6;
    --photo-warm: #c9bfb2;
    --photo-cool: #8f8cb8;
    --ink: #161218;
    --rule: #5a5060;
  }
  * { box-sizing: border-box; margin: 0; padding: 0; }
  html, body { width: 1200px; height: 1000px; overflow: hidden; background: var(--stage); }
  .canvas { position: relative; width: 1200px; height: 1000px; }

  .card {
    position: absolute; left: 290px; width: 622px; height: 374px;
    overflow: hidden; color: var(--ink); text-align: center;
  }
  .card--front { top: 136px; }
  .card--back { top: 541px; }

  .card__backdrop {
    position: absolute; inset: 0;
    background:
      radial-gradient(ellipse 140px 120px at 12% 82%, var(--light-blue) 0%, transparent 70%),
      radial-gradient(ellipse 160px 140px at 92% 78%, var(--peach) 0%, transparent 70%),
      radial-gradient(ellipse 90px 160px at 86% 22%, var(--turquoise) 0%, transparent 70%),
      radial-gradient(ellipse 120px 150px at 32% 10%, var(--pink) 0%, transparent 70%),
      radial-gradient(ellipse 200px 150px at 50% 85%, var(--lavender-deep) 0%, transparent 70%),
      radial-gradient(ellipse 140px 100px at 20% 60%, var(--pink) 0%, transparent 70%),
      var(--lavender);
  }

  .line { position: absolute; left: 0; right: 0; white-space: nowrap; }

  .contact__name { top: 44px; font: 28px/1 "Arimo", Arial, sans-serif; }
  .contact__phone { top: 85px; font: 17px/1 "Arimo", Arial, sans-serif; }
  .contact__email { top: 111px; font: 17px/1 "Arimo", Arial, sans-serif; }

  .brand__name { font: 38px/1 "Marcellus", Georgia, serif; letter-spacing: 0.3px; }
  .brand__tagline { font: 18.5px/1 "Marcellus", Georgia, serif; text-transform: uppercase; letter-spacing: 0.4px; }
  .brand__rule {
    position: absolute; left: 50%; width: 95px; height: 1px;
    margin-left: -47px; background: var(--rule);
  }

  .card--front .brand__name { top: 185px; }
  .card--front .brand__tagline { top: 264px; }
  .card--front .brand__rule { top: 304px; }
  .location { top: 324px; font: 17px/1 "Arimo", Arial, sans-serif; }

  .card--back .brand__name { top: 255px; }
  .card--back .brand__tagline { top: 312px; }

  .tub-photo {
    position: absolute; left: 158px; top: 37px; width: 305px; height: 170px;
    background: linear-gradient(160deg, var(--photo-warm) 0%, var(--photo-cool) 100%);
  }
</style>
</head>
<body>
<div class="canvas">

  <section class="card card--front">
    <div class="card__backdrop" role="img" aria-label="Soft close-up of pastel lavender, pink and blue bath bombs"></div>
    <p class="line contact__name">Donna Pickett</p>
    <p class="line contact__phone">1.702.555.0143</p>
    <p class="line contact__email">dpickett47@mailpost.example</p>
    <p class="line brand__name">Miss Poppy's Soak Parlour</p>
    <p class="line brand__tagline">Maker of Bath Bombs &amp; Bath Salts</p>
    <div class="brand__rule"></div>
    <p class="line location">Las Vegas Nevada</p>
  </section>

  <section class="card card--back">
    <div class="card__backdrop" role="img" aria-label="Soft close-up of pastel lavender, pink and blue bath bombs"></div>
    <div class="tub-photo" role="img" aria-label="Photo of a white claw-foot bathtub filled with swirling blue bath bomb water"></div>
    <p class="line brand__name">Miss Poppy's Soak Parlour</p>
    <p class="line brand__tagline">Maker of Bath Bombs &amp; Bath Salts</p>
  </section>

</div>
</body>
</html>
```